Business Brochure for Painting and Landscape Company

Hi, I was looking to have a brochure made for my business. A brochure I can pass around town. My company offers painting and landscaping services for domestic and commercial properties. some of the service we offer for painting are Drywall Repair, Interior Painting, Exterior Painting, Power Washing, Wallpapering, texture coating, stucco repair, texture removal. For landscape, we offer Lawn Maintenance Garden Care, Trimming, Leaf Removal, Mulching, Pressure Washing, and General Clean-Up. I attached a picture of the business logo but not sure if I need to supply the context that will be in the brochure.

Target Market(s)

Commercial Properties

Industry/Entity Type

Business

Font styles to use
Serif

Colors
0792cd

Requirements
Must have
• Logo on the front and mention that we offer panting and landscaping services. I would like for the brochure to follow the same colors as the logo. It is very important that the brochure highlights that we offer painting and landscaping services.
Nice to have
• To be honest, I don't have an idea on how it should look so I'm open to see what kind of creative ideas there are. I do need it to look professional tho. It would be nice if the brochure can include the lead certified icon attached and the vdrk logo. also an area for an introduction to our company and a section for how to contact us. I uploaded a letter that I plan to include with the brochure (maybe there it'll help with the brochure idea).

```html
<!DOCTYPE html>
<html lang="en">
<head>
<meta charset="utf-8">
<title>KRM Services and Maintenance – Brochure</title>
<link href="https://fonts.googleapis.com/css2?family=Montserrat:wght@600;700;800&family=Raleway:wght@400;500&display=swap" rel="stylesheet">
<style>
  :root{
    --blue:#1769c4;
    --blue-deep:#0f58a8;
    --ink:#2b2b2b;
    --white:#ffffff;
    --page:#ececec;
  }
  *{margin:0;padding:0;box-sizing:border-box}
  html,body{width:960px;height:1200px;overflow:hidden;background:var(--page)}
  .canvas{position:relative;width:960px;height:1200px;overflow:hidden}
  .stage{position:absolute;left:0;top:0;width:1200px;height:1500px;transform:scale(.8);transform-origin:0 0}
  .spread{position:absolute;background:var(--white);box-shadow:0 4px 14px rgba(0,0,0,.25);overflow:hidden;font-family:"Raleway",sans-serif;color:var(--ink)}
  .spread--outside{left:158px;top:57px;width:885px;height:682px}
  .spread--inside{left:158px;top:778px;width:875px;height:676px}
  .spread svg.shapes{position:absolute;left:0;top:0}
  .txt{position:absolute}
  .intro{left:30px;top:56px;width:222px;font-size:16px;line-height:1.2;color:var(--white)}
  .brand{position:absolute;text-align:left}
  .brand-name{font-family:"Montserrat",sans-serif;font-weight:800;color:var(--blue);letter-spacing:1px;line-height:.9}
  .brand-tag{font-family:"Montserrat",sans-serif;font-weight:600;color:#333;letter-spacing:.3px}
  .brand--large{left:605px;top:82px}
  .brand--large .brand-name{font-size:66px}
  .brand--large .brand-tag{font-size:12.5px;margin-top:2px}
  .brand--small{left:312px;top:306px}
  .brand--small .brand-name{font-size:48px}
  .brand--small .brand-tag{font-size:10px;margin-top:1px}
  .contact{left:310px;top:380px;list-style:none}
  .contact li{display:flex;align-items:center;gap:8px;font-size:13px;height:23px}
  .contact li.phone{font-size:18px;color:var(--blue);letter-spacing:1px;height:28px}
  .contact svg{flex:none}
  .badges{left:312px;top:498px;display:flex;gap:18px;align-items:center}
  .badge-square{width:46px;height:56px;background:#16365f}
  .badge-round{width:66px;height:50px;border-radius:50%;background:#3f9a4a;border:3px solid #b7d8b0}
  .headline{left:605px;top:612px;font-family:"Montserrat",sans-serif;font-weight:700;font-size:20.5px;line-height:1.3;color:var(--white)}
  h2{font-family:"Montserrat",sans-serif;font-weight:700;font-size:20px;line-height:1.2;color:var(--blue)}
  .about h2{color:var(--white);margin-left:12px;margin-bottom:18px}
  .about{left:28px;top:28px;width:245px;color:var(--white);font-size:12.3px;line-height:1.2}
  .about p+p{margin-top:14px}
  .body{font-size:12.3px;line-height:1.2}
  .painting{left:386px;top:20px;width:192px}
  .painting h2{margin-bottom:6px}
  .landscape{left:315px;top:378px;width:250px}
  .landscape h2{margin-bottom:6px}
  .better{left:591px;top:362px;width:200px}
  .better h2{margin-bottom:6px}
  .better p+p{margin-top:14px}
  .checklist{list-style:none;margin-top:12px;margin-left:-8px}
  .checklist li{display:flex;align-items:center;gap:7px;font-size:13px;height:23.4px}
  .landscape .checklist{margin-left:-3px;margin-top:14px}
  .cta{left:733px;top:594px;color:var(--white);font-family:"Montserrat",sans-serif;font-weight:600}
  .cta-line{font-size:16px;line-height:1.25}
  .cta-phone{font-size:20px;font-weight:700;margin-top:8px;letter-spacing:.5px}
</style>
</head>
<body>
<div class="canvas">
  <svg width="0" height="0" style="position:absolute" aria-hidden="true">
    <defs>
      <symbol id="tickbox" viewBox="0 0 16 16">
        <rect x="1" y="3" width="12" height="12" fill="none" stroke="#1769c4" stroke-width="1.6"/>
        <path d="M4 8.5 L7 12 L15 1" fill="none" stroke="#1769c4" stroke-width="2"/>
      </symbol>
      <linearGradient id="g-family" x1="0" y1="0" x2="0" y2="1"><stop offset="0" stop-color="#c9d3d6"/><stop offset=".55" stop-color="#8a7a6c"/><stop offset="1" stop-color="#5d9a3a"/></linearGradient>
      <linearGradient id="g-painters" x1="0" y1="0" x2="0" y2="1"><stop offset="0" stop-color="#f4f4f2"/><stop offset="1" stop-color="#3f6fb0"/></linearGradient>
      <linearGradient id="g-gardener" x1="0" y1="0" x2="0" y2="1"><stop offset="0" stop-color="#4f7a3a"/><stop offset=".5" stop-color="#6b6f78"/><stop offset="1" stop-color="#3e8a2e"/></linearGradient>
      <linearGradient id="g-window" x1="0" y1="0" x2="0" y2="1"><stop offset="0" stop-color="#b9b8c2"/><stop offset=".6" stop-color="#8fb0cf"/><stop offset="1" stop-color="#9a9a9a"/></linearGradient>
      <linearGradient id="g-roller" x1="0" y1="0" x2="0" y2="1"><stop offset="0" stop-color="#f2f2f2"/><stop offset="1" stop-color="#d9dbe0"/></linearGradient>
      <linearGradient id="g-garden" x1="0" y1="0" x2="0" y2="1"><stop offset="0" stop-color="#cfcab8"/><stop offset=".45" stop-color="#5f8a3c"/><stop offset="1" stop-color="#6fb83a"/></linearGradient>
      <linearGradient id="g-mower" x1="0" y1="0" x2="0" y2="1"><stop offset="0" stop-color="#3e5a2a"/><stop offset=".5" stop-color="#d9b020"/><stop offset="1" stop-color="#7cc23e"/></linearGradient>
    </defs>
  </svg>

  <div class="stage">
    <section class="spread spread--outside">
      <svg class="shapes" width="885" height="682" viewBox="0 0 885 682">
        <rect width="885" height="682" fill="#fff"/>
        <path d="M0 0 L360 0 C405 70 385 205 300 255 C200 312 100 380 108 500 C114 590 180 642 222 682 L0 682 Z" fill="var(--blue)"/>
        <path d="M885 330 C862 420 760 445 640 472 C530 500 478 600 560 682 L885 682 Z" fill="var(--blue)"/>
        <g>
          <circle cx="148" cy="336" r="132" fill="#fff"/>
          <circle cx="148" cy="336" r="126" fill="var(--blue)"/>
          <circle cx="148" cy="336" r="121" fill="url(#g-family)" role="img" aria-label="Photo of a smiling family lying on a lawn in front of a modern home"/>
        </g>
        <g>
          <circle cx="654" cy="300" r="112" fill="#fff" stroke="var(--blue)" stroke-width="4"/>
          <circle cx="654" cy="300" r="104" fill="url(#g-painters)" role="img" aria-label="Photo of two painters in hard hats working on a white wall"/>
        </g>
        <g>
          <circle cx="752" cy="474" r="122" fill="#fff"/>
          <circle cx="752" cy="474" r="116" fill="var(--blue)"/>
          <circle cx="752" cy="474" r="111" fill="url(#g-gardener)" role="img" aria-label="Photo of a gardener trimming a hedge"/>
        </g>
      </svg>

      <p class="txt intro">We would cherish an opportunity to demonstrate what we can do. We are capable of working within a budget and are available to work on weekends.</p>

      <div class="brand brand--large">
        <div class="brand-name">KRM</div>
        <div class="brand-tag">Services and Maintenance</div>
      </div>

      <div class="brand brand--small">
        <div class="brand-name">KRM</div>
        <div class="brand-tag">Services and Maintenance</div>
      </div>

      <ul class="txt contact">
        <li class="phone">
          <svg width="18" height="18" viewBox="0 0 18 18"><circle cx="9" cy="9" r="8" fill="none" stroke="#1769c4" stroke-width="1.5"/><path d="M6 4.5 L7.5 4.5 L8.3 7 L7.2 7.8 C7.8 9.2 8.8 10.2 10.2 10.8 L11 9.7 L13.5 10.5 L13.5 12 C13.5 12.8 12.8 13.4 12 13.3 C8.3 12.8 5.2 9.7 4.7 6 C4.6 5.2 5.2 4.5 6 4.5 Z" fill="#1769c4"/></svg>
          (555)014-2290
        </li>
        <li>
          <svg width="13" height="13" viewBox="0 0 14 14"><circle cx="7" cy="7" r="6" fill="none" stroke="#1769c4" stroke-width="1.1"/><ellipse cx="7" cy="7" rx="2.6" ry="6" fill="none" stroke="#1769c4" stroke-width="1"/><path d="M1 7 H13 M2 4 H12 M2 10 H12" stroke="#1769c4" stroke-width="1"/></svg>
          KRMServicesandMaintenance.com
        </li>
        <li>
          <svg width="13" height="13" viewBox="0 0 14 14"><rect x="1" y="3" width="12" height="8" fill="none" stroke="#1769c4" stroke-width="1.1"/><path d="M1 3 L7 8 L13 3" fill="none" stroke="#1769c4" stroke-width="1.1"/></svg>
          hello@KRMServicesandMaintenance.com
        </li>
        <li>
          <svg width="13" height="13" viewBox="0 0 14 14"><rect x="3" y="1" width="8" height="12" fill="none" stroke="#1769c4" stroke-width="1.1"/><path d="M5 4 H9 M5 7 H9 M5 10 H9" stroke="#1769c4" stroke-width="1"/></svg>
          CSL# 20417
        </li>
      </ul>

      <div class="txt badges">
        <div class="badge-square" role="img" aria-label="vdrk licence badge"></div>
        <div class="badge-round" role="img" aria-label="Certification badge"></div>
      </div>

      <p class="txt headline">QUALITY PAINTING AND<br>LANDSCAPING SERVICES</p>
    </section>

    <section class="spread spread--inside">
      <svg class="shapes" width="875" height="676" viewBox="0 0 875 676">
        <rect width="875" height="676" fill="#fff"/>
        <path d="M0 0 L345 0 C385 80 362 172 272 222 C150 290 88 340 88 452 C88 562 180 632 252 676 L0 676 Z" fill="var(--blue)"/>
        <path d="M682 0 L875 0 L875 676 L560 676 C690 650 770 600 805 520 C830 440 790 330 722 262 C660 200 636 70 682 0 Z" fill="var(--blue)"/>
        <g>
          <circle cx="732" cy="128" r="113" fill="#fff"/>
          <circle cx="732" cy="128" r="107" fill="var(--blue)"/>
          <circle cx="732" cy="128" r="102" fill="url(#g-window)" role="img" aria-label="Photo of a painter masking a window on a house exterior"/>
        </g>
        <g>
          <circle cx="620" cy="257" r="86" fill="#fff" stroke="var(--blue)" stroke-width="4"/>
          <circle cx="620" cy="257" r="80" fill="url(#g-roller)" role="img" aria-label="Photo of a painter with a paint roller"/>
        </g>
        <g>
          <circle cx="167" cy="353" r="118" fill="#fff"/>
          <circle cx="167" cy="353" r="112" fill="var(--blue)"/>
          <circle cx="167" cy="353" r="107" fill="url(#g-garden)" role="img" aria-label="Photo of a landscaped front garden with flower beds and lawn"/>
        </g>
        <g>
          <circle cx="192" cy="563" r="88" fill="#fff" stroke="var(--blue)" stroke-width="4"/>
          <circle cx="192" cy="563" r="81" fill="url(#g-mower)" role="img" aria-label="Photo of a ride-on mower cutting grass"/>
        </g>
      </svg>

      <div class="txt about">
        <h2>ABOUT US</h2>
        <p>We are a family owned business that specializes in Painting and Landscaping Services for commercial properties. We have been in business for over five years, having completed over 300 commercial projects in that time.</p>
        <p>We possess the equipment, transporta­tion, and staff needed to complete any scope of work on time and as instructed.</p>
      </div>

      <div class="txt painting body">
        <h2>PAINTING<br>SERVICES</h2>
        <p>We specializes in exceptional interior and exterior commercial and residential painting projects. Services we offer :</p>
        <ul class="checklist">
          <li><svg width="16" height="16"><use href="#tickbox"/></svg>Drywall Repair</li>
          <li><svg width="16" height="16"><use href="#tickbox"/></svg>Interior Painting</li>
          <li><svg width="16" height="16"><use href="#tickbox"/></svg>Exterior Painting</li>
          <li><svg width="16" height="16"><use href="#tickbox"/></svg>Power Washing</li>
          <li><svg width="16" height="16"><use href="#tickbox"/></svg>Wallpapering</li>
          <li><svg width="16" height="16"><use href="#tickbox"/></svg>Texture coating</li>
          <li><svg width="16" height="16"><use href="#tickbox"/></svg>Stucco repair</li>
          <li><svg width="16" height="16"><use href="#tickbox"/></svg>Texture removal.</li>
        </ul>
      </div>

      <div class="txt landscape body">
        <h2>LANDSCAPING<br>SERVICES</h2>
        <p>We offer a variety of residential and commercial landscaping design services that include:</p>
        <ul class="checklist">
          <li><svg width="16" height="16"><use href="#tickbox"/></svg>Lawn Maintenance</li>
          <li><svg width="16" height="16"><use href="#tickbox"/></svg>Garden Care</li>
          <li><svg width="16" height="16"><use href="#tickbox"/></svg>Trimming</li>
          <li><svg width="16" height="16"><use href="#tickbox"/></svg>Leaf Removal</li>
          <li><svg width="16" height="16"><use href="#tickbox"/></svg>Mulching</li>
          <li><svg width="16" height="16"><use href="#tickbox"/></svg>Pressure Washing,</li>
          <li><svg width="16" height="16"><use href="#tickbox"/></svg>General Clean-Up.</li>
        </ul>
      </div>

      <div class="txt better body">
        <h2>WHAT MAKES<br>US BETTER?</h2>
        <p>What sets our company apart from the rest is our commitment to quality. We committed to delivering the best quality of work available and exceeding your expectations.</p>
        <p>We always remain courteous, transparent, and above all else, professional with our clients.</p>
      </div>

      <div class="txt cta">
        <div class="cta-line">Call us today for<br>free estimate</div>
        <div class="cta-phone">555 014 2290</div>
      </div>
    </section>
  </div>
</div>
</body>
</html>
```